Inflatable Movie Screen company needs a Brochure Design for sales kit

We need a brochure as per attached sketch drawing which is to:
1)follow the sample layout
2) attached images must be used
3) to follow company corporate colors or suggest something professional and appropriate for the theme
Updates

Target Market(s)

Corporate and Community Clubs

Industry/Entity Type

Entertainment

Requirements
Must have
• Colors to be in line with corporate colors OR to suggest something appropriate.
Nice to have
• A unique concept
Should not have
• Too fanciful

```html
<!DOCTYPE html>
<html lang="en">
<head>
<meta charset="utf-8">
<title>Lumara Events – Brochure Cover</title>
<link rel="stylesheet" href="https://fonts.googleapis.com/css2?family=Cabin:wght@400;600&display=swap">
<style>
  :root {
    --paper: #ffffff;
    --page-edge: #b9b9b9;
    --blue-deep: #2f7fe6;
    --blue-mid: #7fb4ef;
    --blue-pale: #d3e6fa;
    --ink-grey: #7b7b7b;
    --ink-grey-dark: #6a6a6a;
  }
  html, body {
    margin: 0;
    padding: 0;
    width: 845px;
    height: 1200px;
    overflow: hidden;
    background: var(--paper);
  }
  .cover {
    position: relative;
    width: 845px;
    height: 1200px;
    box-sizing: border-box;
    border: 1px solid var(--page-edge);
    background: var(--paper);
    overflow: hidden;
    font-family: "Cabin", sans-serif;
  }
  .cover-artwork {
    position: absolute;
    inset: 0;
    background: linear-gradient(150deg,
      var(--blue-mid) 0%,
      var(--blue-deep) 28%,
      var(--blue-mid) 48%,
      var(--blue-pale) 66%,
      var(--paper) 80%);
    opacity: 0.75;
  }
  .brand {
    position: absolute;
    left: 50px;
    top: 950px;
    color: var(--ink-grey);
    font-weight: 400;
  }
  .brand-name {
    margin: 0;
    font-size: 76px;
    font-weight: 400;
    line-height: 1;
    letter-spacing: 5px;
    text-transform: uppercase;
  }
  .brand-legal {
    margin: 10px 0 0 44px;
    font-size: 12px;
    letter-spacing: 2px;
    text-transform: uppercase;
  }
  .contact-list {
    position: absolute;
    left: 52px;
    top: 1080px;
    margin: 0;
    padding: 0;
    list-style: none;
    color: var(--ink-grey-dark);
    font-weight: 600;
    font-size: 21px;
    line-height: 29px;
  }
</style>
</head>
<body>
<main class="cover">
  <div class="cover-artwork" role="img" aria-label="Cover artwork: flowing translucent blue ribbons sweeping diagonally across the page"></div>

  <header class="brand">
    <h1 class="brand-name">Lumara</h1>
    <p class="brand-legal">Lumara Events Pte Ltd</p>
  </header>

  <ul class="contact-list">
    <li class="contact-item">Contact</li>
    <li class="contact-item">Address</li>
    <li class="contact-item">Webpage</li>
  </ul>
</main>
</body>
</html>
```